Harbor Tandem Web Design Project

We need a website design for a start up company called "Harbor Tandem". We provide business consultancy services as well as technology-related services (IT). The design should communicate simplicity and elegance. The domain name of the site will be harbortandem.com. The logo of the company is https://files.pinvault.net/u/8147206/7730_2049185_31947_image.jpg
Updates

Target Market(s)

SMB, Corporates, Semi-governments, Governments.

Industry/Entity Type

Business

Requirements
Must have
• - The background of the pages should be white or soft grey, but we are open for suggestions.
- The pages should have nice menu animations.
- The pages should be "portal-style", with multiple placeholders for different sections and multiple tabs.
Nice to have
• The page should auto-fit the screen and scroll vertically as much as needed.
Should not have
• - Flash Animations.
- Generic Photos.

```html
<!DOCTYPE html>
<html lang="en">
<head>
<meta charset="utf-8">
<title>Harbor Tandem</title>
<link href="https://fonts.googleapis.com/css2?family=PT+Sans+Narrow:wght@400;700&display=swap" rel="stylesheet">
<style>
:root{
  --ink:#3d3d3d;
  --body:#555;
  --muted:#777;
  --accent:#4aa3cf;
  --link:#2a6db0;
  --red:#d7282a;
  --red-dark:#a9161a;
  --rule:#e3e3e3;
  --hero:#eeeeee;
  --footer:#333333;
}
*{box-sizing:border-box;margin:0;padding:0}
html,body{width:1120px;height:1200px;overflow:hidden;background:#fff}
body{position:relative;font-family:"PT Sans Narrow",sans-serif;color:var(--body)}
.abs{position:absolute}

/* header */
.brand{left:162px;top:26px;display:flex;align-items:center;gap:8px;font-size:24px;font-weight:700;color:var(--link)}
.brand-dot{width:18px;height:18px;border-radius:50%;background:var(--link)}
.nav{top:33px;left:0;width:1120px;height:16px;font-size:12.5px;letter-spacing:.6px;color:#888}
.nav a{position:absolute;color:inherit;text-decoration:none}
.nav a.current{color:var(--accent)}

/* hero */
.hero{left:0;top:80px;width:1120px;height:326px;background:radial-gradient(ellipse at 60% 40%,#f7f7f7,#e9e9e9 75%);border-top:1px solid #dcdcdc;border-bottom:1px solid #dcdcdc}
.hero-title{left:172px;top:140px;font-size:38px;line-height:37px;font-weight:700;letter-spacing:2px;color:#555}
.hero-sub{left:173px;top:227px;font-size:15px;font-weight:700;letter-spacing:.6px;color:var(--accent)}
.hero-copy{left:173px;top:262px;width:350px;font-size:10px;line-height:14.5px;letter-spacing:.5px;color:#666}
.btn{display:flex;align-items:center;justify-content:center;background:linear-gradient(#e95454,var(--red) 55%,var(--red-dark));border:1px solid #a51d1f;border-radius:2px;color:#5a0c0d;font-size:14px;font-weight:700;letter-spacing:1px;box-shadow:inset 0 1px 0 rgba(255,255,255,.35)}
.hero-btn{left:173px;top:312px;width:158px;height:31px}
.hero-art{left:564px;top:100px;width:396px;height:252px;background:linear-gradient(#eaf4fa 0%,#f1f1f1 55%,#e6e6e6 100%);border-radius:4px}

/* intro */
.intro{left:0;top:428px;width:1120px;text-align:center;font-size:16px;font-weight:700;letter-spacing:.6px;color:var(--ink)}
.intro span{color:var(--accent)}
.rule{height:1px;background:var(--rule)}

/* features */
.card{top:485px;width:187px}
.card-photo{height:118px}
.card h3{margin-top:17px;padding-bottom:5px;border-bottom:1px solid var(--rule);font-size:12.5px;font-weight:400;letter-spacing:.4px;color:var(--link)}
.card p{margin-top:7px;font-size:9.6px;line-height:16px;letter-spacing:.5px;color:#666}

/* call to action */
.cta{left:160px;top:716px;width:802px;height:69px;border:1px solid #dedede;background:#fafafa}
.cta h2{position:absolute;left:14px;top:13px;font-size:15.5px;letter-spacing:.7px;color:var(--ink)}
.cta p{position:absolute;left:14px;top:36px;font-size:9.4px;letter-spacing:.6px;color:#666}
.cta .btn{position:absolute;left:628px;top:17px;width:158px;height:31px}

/* tabs */
.tab{top:825px;height:37px;border:1px solid #e6e6e6;border-bottom:none;background:linear-gradient(#fff,#f3f3f3);display:flex;align-items:center;justify-content:center;font-size:11.5px;letter-spacing:2.2px;color:#888}
.tab.active{top:814px;height:49px;background:#fff;color:var(--link);font-size:13px;border-top:2px solid #ececec;z-index:2}
.panel{left:162px;top:862px;width:797px;height:300px;border:1px solid #e6e6e6;border-bottom:none;background:#fff}
.panel h2{position:absolute;left:19px;top:26px;font-size:18px;letter-spacing:1px;color:var(--ink)}
.panel .rule{position:absolute;left:19px;top:56px;width:726px}
.panel-copy{position:absolute;left:19px;top:72px;width:410px;font-size:10px;line-height:24px;letter-spacing:.3px;color:#666}
.panel-copy p{margin:0}
.hl{color:var(--red)}
.panel-side{position:absolute;left:468px;top:76px}
.panel-side h3{font-size:13.5px;letter-spacing:.5px;color:var(--ink)}
.panel-side ul{list-style:none;margin-top:12px}
.panel-side li{position:relative;padding-left:15px;height:28.8px;font-size:10px;letter-spacing:.3px;color:var(--link)}
.panel-side li::before{content:"";position:absolute;left:1px;top:2px;border-left:5px solid #444;border-top:3.5px solid transparent;border-bottom:3.5px solid transparent}

/* footer */
.footer{left:0;top:1158px;width:1120px;height:42px;background:var(--footer);font-size:8.6px;color:#aaa;letter-spacing:.2px}
.footer a{position:absolute;top:17px;color:inherit;text-decoration:none}
.footer a.current{color:var(--accent)}
.footer .legal{position:absolute;right:161px;top:17px}
.footer .legal span{color:var(--accent)}
</style>
</head>
<body>

<header>
  <div class="abs brand"><span class="brand-dot"></span>Harbor Tandem</div>
  <nav class="abs nav">
    <a class="current" style="left:540px">home</a>
    <a style="left:634px">about</a>
    <a style="left:713px">work</a>
    <a style="left:785px">blog</a>
    <a style="left:856px">faq</a>
    <a style="left:921px">contact</a>
  </nav>
</header>

<section class="abs hero"></section>
<h1 class="abs hero-title">Phasellus alimueter<br>fementum eros allen</h1>
<p class="abs hero-sub">Nelementum velit erting toning ellening tarbons</p>
<p class="abs hero-copy">Lorem ipsum dolor sit amet, consectetur adipiscing elit. Nulla blandit ante at risus auctor aliquam non non eroson. Vestibulum pretiuming terney geretable</p>
<a class="abs btn hero-btn">Get Started</a>
<div class="abs hero-art" role="img" aria-label="Illustration of a blue cloud linked by arrows to servers, a desktop, a laptop, a tablet and a phone"></div>

<h2 class="abs intro">Donec fringilla, massa sit amet auctor tristique, velit lectus <span>elementum velit erting toning</span></h2>
<div class="abs rule" style="left:160px;top:467px;width:800px"></div>

<article class="abs card" style="left:162px">
  <div class="card-photo" role="img" aria-label="Photo of a hand pointing at charts on a monitor" style="background:linear-gradient(135deg,#c9d3df,#8e9fb3)"></div>
  <h3>Donec fringilla</h3>
  <p>Lorem ipsum dolor sit amet, consectetur adipiscing elit. Nulla blandit ante at risus</p>
</article>
<article class="abs card" style="left:365px">
  <div class="card-photo" role="img" aria-label="Photo of hands holding a card above a tablet and a coffee cup" style="background:linear-gradient(#9dbde0,#c7a58b)"></div>
  <h3>Donec fringilla</h3>
  <p>Lorem ipsum dolor sit amet, consectetur adipiscing elit. Nulla blandit ante at risus</p>
</article>
<article class="abs card" style="left:569px">
  <div class="card-photo" role="img" aria-label="Photo of a person working on a laptop" style="background:linear-gradient(135deg,#7fa8c9,#d8c2a8)"></div>
  <h3>Donec fringilla</h3>
  <p>Lorem ipsum dolor sit amet, consectetur adipiscing elit. Nulla blandit ante at risus</p>
</article>
<article class="abs card" style="left:773px">
  <div class="card-photo" role="img" aria-label="Photo of a hand on a computer mouse beside a keyboard" style="background:linear-gradient(135deg,#e7ecef,#9aa3ab)"></div>
  <h3>Donec fringilla</h3>
  <p>Lorem ipsum dolor sit amet, consectetur adipiscing elit. Nulla blandit ante at risus</p>
</article>

<section class="abs cta">
  <h2>Mauris rutrum ante mattis neque pellentesque</h2>
  <p>Integer rutrum nunc eu dui rutrum vel cursus purus fermentum. Duis mattis odio id erat vestibulum bibendum elenrotte eke</p>
  <a class="btn">Get Started</a>
</section>

<div class="abs tab active" style="left:162px;width:223px">Tab Heading</div>
<div class="abs tab" style="left:385px;width:190px">Tab Heading</div>
<div class="abs tab" style="left:575px;width:192px">Tab Heading</div>
<div class="abs tab" style="left:767px;width:192px">Tab Heading</div>

<section class="abs panel">
  <h2>Phasellus aliquet fermentum eros allen</h2>
  <div class="rule"></div>
  <div class="panel-copy">
    <p>Lorem ipsum dolor sit amet, consectetur adipiscing elit. Nulla blandit ante at risus auctor aliquam non non eroson. Vestibulum pretium <span class="hl">blandit nisl in</span> laoreet. Suspendisse ut auctor diam. Vestibulum gravida adipiscing leo, non <span class="hl">tempus quam</span> scelerisque annelre gingelrty edertserbii ellerting yun iouksble.</p>
    <p>Vestibulum pretium <span class="hl">blandit nisl in</span> laoreet. Suspendisse ut auctor diam. Vestibulum gravida adipiscing leo, non tempus quam scelerisque a.</p>
  </div>
  <div class="panel-side">
    <h3>Lorem ipsum deler</h3>
    <ul>
      <li>Lorem ipsum dolor sit amet, consectetur adipiscing</li>
      <li>Nulla blandit ante at risus auctor aliquam non non</li>
      <li>Lorem ipsum dolor sit amet, consectetur adipiscing</li>
      <li>Nulla blandit ante at risus auctor aliquam eroson</li>
    </ul>
  </div>
</section>

<footer class="abs footer">
  <a class="current" style="left:159px">Home</a>
  <a style="left:208px">Services</a>
  <a style="left:266px">Blog</a>
  <a style="left:311px">Guarantee</a>
  <a style="left:374px">Contact</a>
  <div class="legal">Copyright © 2012 &nbsp;<span>Harbor Tandem</span> | All rights reserved</div>
</footer>

</body>
</html>
```